Holiday Rental Leaflet

Want a DL size double sided leaflet to distribute via local businesses, markets, family and friends
HOLIDAY RENTALCarrickalinga - 17 Farrow Street Sleeps 8-10 (2 Queen, 1 Double, 2 bunks), 4 bedrooms, BIR to all bedrooms 2 Bathrooms, one with bath, 2 toilets Open Plan Lounge/Dining/Kitchen area Dining Table for 8 peopleReverse cycle airconditionerSlow combustion wood heaterTV/DVD, CD/RadioKitchen has m/wave, oven, fridge/freezer, dishwasherBBQ providedTimber decking with 2 outside tables and 12 chairs Washing Machine and dryer provided One street back from beach Smoke free zone No Pets
For further information or to book contact Joan on 0491 278 306 or email joanbirch62@veltranet.com.au

Requirements
Nice to have
• Have sent a variety of photos of the house. No need to use all of them, pick out the most relevant for the leaflet.

```html
<!DOCTYPE html>
<html lang="en">
<head>
<meta charset="utf-8">
<title>Holiday Rental – Carrickalinga</title>
<link href="https://fonts.googleapis.com/css2?family=Cinzel:wght@700;900&family=Roboto+Condensed:wght@700&family=Open+Sans:wght@700&display=swap" rel="stylesheet">
<style>
  :root {
    --sand: #d8bf9f;
    --sand-light: #e6d3b8;
    --sand-dark: #c9ab88;
    --title-red: #e8174f;
    --phone-red: #e8174f;
    --ink: #1b1b1b;
    --bullet-blue: #4a86c5;
    --address-blue: #5b8dc4;
    --frame-white: #ffffff;
    --frame-beige: #ecdcbc;
  }
  html, body { margin: 0; padding: 0; overflow: hidden; }
  body { width: 1200px; height: 596px; background: var(--sand); }
  .leaflet {
    position: relative; width: 1200px; height: 596px; overflow: hidden;
    background: radial-gradient(ellipse at 30% 40%, var(--sand-light), var(--sand) 60%, var(--sand-dark));
    font-family: "Roboto Condensed", "Arial Narrow", sans-serif;
    color: var(--ink);
  }
  .shell-decor {
    position: absolute; left: 735px; top: -10px; width: 175px; height: 70px;
    border-radius: 50%;
    background: radial-gradient(ellipse, #c98a5e, #e4c2a0 70%, transparent 72%);
  }
  .shell-decor--small {
    left: 200px; top: -20px; width: 60px; height: 35px;
    background: radial-gradient(ellipse, #efe3d2, transparent 70%);
  }
  .title {
    position: absolute; left: 70px; top: 14px; margin: 0;
    font-family: "Cinzel", "Times New Roman", serif; font-weight: 900;
    font-size: 66px; letter-spacing: 1px; color: var(--title-red); line-height: 1;
  }
  .title .cap { font-size: 84px; }
  .gallery {
    position: absolute; left: 18px; top: 100px; width: 481px; height: 480px;
    background: var(--frame-white);
  }
  .gallery .photo { position: absolute; width: 153px; height: 153px; }
  .features {
    position: absolute; left: 510px; top: 134px; margin: 0; padding: 0;
    list-style: none; font-size: 17.5px; line-height: 24.7px;
  }
  .features li { position: relative; padding-left: 20px; }
  .features li::before {
    content: ""; position: absolute; left: 0; top: 6px;
    width: 13px; height: 13px; border-radius: 50%; background: var(--bullet-blue);
  }
  .address {
    position: absolute; right: 48px; top: 58px; text-align: left;
    font-family: "Open Sans", Arial, sans-serif; font-weight: 700;
    font-size: 24px; line-height: 31px; color: var(--address-blue);
  }
  .contact {
    position: absolute; left: 880px; top: 148px; width: 290px; text-align: center;
    font-size: 18px; line-height: 22px;
  }
  .contact .phone {
    display: flex; align-items: center; justify-content: center; gap: 6px;
    margin: 2px 0; font-family: "Open Sans", Arial, sans-serif;
    font-size: 29px; line-height: 34px; color: var(--phone-red);
  }
  .beach-frame {
    position: absolute; left: 873px; top: 287px; width: 296px; height: 288px;
    background: var(--frame-beige);
  }
  .beach-frame .photo {
    position: absolute; left: 12px; top: 8px; width: 275px; height: 272px;
    background: linear-gradient(to bottom, #2d78c9 0%, #6aa6de 40%, #1e6f9a 44%, #2b93a6 60%, #8cc1bf 74%, #d7c7a6 82%, #c9b593 100%);
  }
</style>
</head>
<body>
<div class="leaflet">
  <div class="shell-decor" role="img" aria-label="Seashell lying in the sand"></div>
  <div class="shell-decor shell-decor--small" role="img" aria-label="Small shell in the sand"></div>

  <h1 class="title"><span class="cap">H</span>OLIDAY <span class="cap">R</span>ENTAL</h1>

  <div class="gallery">
    <div class="photo" style="left:7px;top:5px;background:linear-gradient(#a9c8e0,#6d7a58 55%,#7e9a4c)" role="img" aria-label="House exterior on stilts with lawn"></div>
    <div class="photo" style="left:165px;top:5px;background:linear-gradient(#b7cde0 0%,#6d91b4 38%,#2f5f86 60%,#3c6b3a 85%)" role="img" aria-label="Sea view over garden hedge"></div>
    <div class="photo" style="left:323px;top:5px;background:linear-gradient(#b98d5a,#3a3432 60%,#8a7f70)" role="img" aria-label="Lounge with leather sofas and colourful cushions"></div>
    <div class="photo" style="left:7px;top:163px;background:linear-gradient(#d9a268,#c07b3c 60%,#c9c2b5)" role="img" aria-label="Timber-lined dining area with table and chairs"></div>
    <div class="photo" style="left:165px;top:163px;background:linear-gradient(#e7b27a,#8a7866 50%,#5a3f32 80%)" role="img" aria-label="Slow combustion wood heater on stone hearth"></div>
    <div class="photo" style="left:323px;top:163px;background:linear-gradient(#c88a48,#e26c3c 50%,#3f6fb0 80%)" role="img" aria-label="Bedroom with striped bedspread"></div>
    <div class="photo" style="left:7px;top:321px;background:linear-gradient(#b07a45,#4d4038 50%,#6d86a8)" role="img" aria-label="Bunk beds in timber bedroom"></div>
    <div class="photo" style="left:165px;top:321px;background:linear-gradient(#f2f2f2,#d8d8d8 60%,#a7a29c)" role="img" aria-label="White bathroom with bath and toilet"></div>
    <div class="photo" style="left:323px;top:321px;background:linear-gradient(#cfe0ea,#4a5a52 45%,#6e9a4a)" role="img" aria-label="Timber deck with umbrellas and outdoor tables"></div>
  </div>

  <ul class="features">
    <li>Sleeps 8-10&nbsp; (2 Queen, 1 Double, 2 bunks)</li>
    <li>4 bedrooms, BIR to all bedrooms</li>
    <li>2 Bathrooms, one with bath, 2 toilets</li>
    <li>Open Plan Lounge/Dining/Kitchen area</li>
    <li>Dining Table for 8 people</li>
    <li>Reverse cycle airconditioner</li>
    <li>Slow combustion wood heater</li>
    <li>TV/DVD, CD/Radio</li>
    <li>Kitchen has m/wave, oven,<br>fridge/freezer, dishwasher</li>
    <li>BBQ provided</li>
    <li>Timber decking with 2 outside tables<br>and 12 chairs</li>
    <li>Washing Machine and dryer provided</li>
    <li>One street back from beach</li>
    <li>Smoke free zone</li>
    <li>No Pets</li>
  </ul>

  <div class="address">Carrickalinga<br>17 Farrow Street</div>

  <div class="contact">
    For further information or<br>to book contact Joan at
    <div class="phone">
      <svg width="22" height="26" viewBox="0 0 22 26" aria-hidden="true">
        <path d="M15 2 C6 3 3 9 3 13 C3 17 6 23 15 24 L17 18 L13 17 C11 15 11 11 13 9 L17 8 Z" fill="none" stroke="var(--phone-red)" stroke-width="2.4" stroke-linejoin="round"/>
      </svg>
      <span>0491 278 306</span>
    </div>
    or email at<br>joanbirch62@veltranet.com.au
  </div>

  <div class="beach-frame">
    <div class="photo" role="img" aria-label="Calm turquoise sea meeting a sandy beach under blue sky"></div>
  </div>
</div>
</body>
</html>
```